RWT Installations Ltd Business Cards

We need a business card with our business logo. We provide window and door installations on high-rises in west coast British Colombia, Canada.

I would like my business information and details on one side of the card, and the other side the company name with logo

Target Market(s)

General Contractors

Industry/Entity Type

Construction

Contact Information for Business Card

one side i want my company name and logo in the dark theme logo that i provided

Requirements
Must have
• Tomas Verelund, 15559284016, RWTInstallations@mailvera.example, 1408-5192 Pellow Avenue Burnaby BC, V0X 1Z9, Owner & Manager

```html
<!DOCTYPE html>
<html lang="en">
<head>
<meta charset="utf-8">
<title>RWT Installations Ltd – Business Cards</title>
<link href="https://fonts.googleapis.com/css2?family=Raleway:wght@400;500;700&display=swap" rel="stylesheet">
<style>
  :root {
    --backdrop: #b3b3b3;
    --card: #ffffff;
    --brand-blue: #27a8e0;
    --brand-grey: #8e8e8e;
    --ink: #1a1a1a;
    --font-text: "Raleway", sans-serif;
  }
  * { box-sizing: border-box; margin: 0; padding: 0; }
  html, body {
    width: 1200px;
    height: 1200px;
    overflow: hidden;
    background: var(--backdrop);
    font-family: var(--font-text);
  }
  .sheet { position: relative; width: 1200px; height: 1200px; }

  .card {
    position: absolute;
    left: 166px;
    width: 868px;
    height: 507px;
    background: var(--card);
    box-shadow: 0 2px 6px rgba(0,0,0,0.25);
    overflow: hidden;
  }
  .card--front { top: 72px; }
  .card--back { top: 624px; }

  /* wordmark */
  .wordmark {
    display: flex;
    align-items: center;
    color: var(--brand-blue);
    font-weight: 700;
    white-space: nowrap;
  }
  .wordmark__square { background: var(--brand-grey); flex: none; }

  .card--front .wordmark {
    position: absolute;
    left: 87px;
    top: 110px;
    font-size: 36px;
    gap: 16px;
  }
  .card--front .wordmark__square { width: 76px; height: 76px; }

  .card--back .wordmark {
    position: absolute;
    left: 0; right: 0; top: 0; bottom: 0;
    justify-content: center;
    font-size: 44px;
    gap: 22px;
  }
  .card--back .wordmark__square { width: 104px; height: 104px; }

  /* large numeral shape */
  .accent-numeral {
    position: absolute;
    left: 0;
    top: 0;
    width: 868px;
    height: 507px;
  }
  .accent-numeral polygon { fill: var(--brand-blue); }

  /* holder */
  .holder {
    position: absolute;
    right: calc(868px - 315px);
    top: 345px;
    text-align: right;
    white-space: nowrap;
  }
  .holder__name {
    color: var(--brand-blue);
    font-weight: 700;
    font-size: 33px;
    line-height: 1.2;
  }
  .holder__role {
    color: var(--ink);
    font-size: 20px;
    font-weight: 500;
    margin-top: 6px;
  }

  /* contact */
  .contact {
    position: absolute;
    top: 352px;
    left: 340px;
    width: 450px;
    list-style: none;
  }
  .contact__item {
    display: flex;
    justify-content: flex-end;
    align-items: center;
    min-height: 31px;
    font-size: 18px;
    font-weight: 500;
    line-height: 1.3;
    color: var(--ink);
  }
  .contact__item--address { padding-top: 3px; }
  .contact__text { text-align: right; white-space: nowrap; }
  .contact__icon {
    width: 14px;
    height: 14px;
    margin-left: 63px;
    fill: #fff;
    flex: none;
  }
</style>
</head>
<body>
<main class="sheet">

  <section class="card card--front" aria-label="Business card front">
    <svg class="accent-numeral" viewBox="0 0 868 507" aria-hidden="true">
      <polygon points="868,0 627,156 627,205 737,140 737,507 868,507"/>
    </svg>

    <div class="wordmark">
      <span class="wordmark__square" aria-hidden="true"></span>
      <span class="wordmark__name">RWT Installations Ltd</span>
    </div>

    <div class="holder">
      <p class="holder__name">TOMAS VERELUND</p>
      <p class="holder__role">Owner &amp; Manager</p>
    </div>

    <ul class="contact">
      <li class="contact__item">
        <span class="contact__text">15559284016</span>
        <svg class="contact__icon" viewBox="0 0 24 24" aria-hidden="true"><path d="M6.6 10.8a15.1 15.1 0 0 0 6.6 6.6l2.2-2.2a1 1 0 0 1 1-.25 11.4 11.4 0 0 0 3.6.57 1 1 0 0 1 1 1V20a1 1 0 0 1-1 1A17 17 0 0 1 3 4a1 1 0 0 1 1-1h3.5a1 1 0 0 1 1 1c0 1.25.2 2.45.57 3.6a1 1 0 0 1-.25 1z"/></svg>
      </li>
      <li class="contact__item">
        <span class="contact__text">RWTInstallations@mailvera.example</span>
        <svg class="contact__icon" viewBox="0 0 24 24" aria-hidden="true"><path d="M3 5h18a1 1 0 0 1 1 1v12a1 1 0 0 1-1 1H3a1 1 0 0 1-1-1V6a1 1 0 0 1 1-1zm1 2.2V8l8 5 8-5v-.8l-8 5z"/></svg>
      </li>
      <li class="contact__item contact__item--address">
        <span class="contact__text">1408-5192 Pellow Avenue<br>Burnaby BC, V0X 1Z9</span>
        <svg class="contact__icon" viewBox="0 0 24 24" aria-hidden="true"><path d="M12 2a7 7 0 0 0-7 7c0 5.2 7 13 7 13s7-7.8 7-13a7 7 0 0 0-7-7zm0 9.5A2.5 2.5 0 1 1 12 6.5a2.5 2.5 0 0 1 0 5z"/></svg>
      </li>
    </ul>
  </section>

  <section class="card card--back" aria-label="Business card back">
    <div class="wordmark">
      <span class="wordmark__square" aria-hidden="true"></span>
      <span class="wordmark__name">RWT Installations Ltd</span>
    </div>
  </section>

</main>
</body>
</html>
```